Fernhold Capital - Web Design

I have recently established a business called Fernhold Capital. The business is focused on providing property developers with project financing solutions. This is not a real estate website so please do not provide such pics or design. I provide financial solutions.

I have been in the financial markets for the past 20 years covering all asset classes from trading through to portfolio management, structuring and business development. The majority of this time was spent with building new business and expanding into new opportunities.

This is a start-up business so there isn't much content at this stage. Therefore, its all about first impressions. I want a design that portray confidence; and that I can deliver a workable solution. It must provide the perception of sophistication, innovation, yet simplistic so its not trying to deceive/hide something. Most importantly it must give the Client a sense of trust and reliability.

I would like to have the website portray my depth of experience in providing financing solutions and consultancy services in achieving the investment objectives. However, I would like to avoid looking like a one man band. I do have access to resources just not directly employed by the company.

Anyway, I hope this is enough to at least wet your appetite. I recently had a logo created on PixelGuild that should set the theme/style of the website

Project Deadline Extended
Reason: Increase time to allow web designer/developer more time to understand the style I am after.

All, Thank you for your current designs. I am based in Singapore, however, I am currently traveling today but will respond by later tonight or tomorrow. Owen

All, A general observation. Please do not include photos of houses, architectural drawings or images that portal construction or real estate. This implies I am either a property agent or in some way directly involve in selling property...very misleading. Remember, I am involved in provide financial solutions not selling property. Owen

All, Please avoid using numerous people within the site as it may represent that my business has a large number of staff when in fact its only me. However, I also don't want to look like a "one man band". So be balanced on using people - I am not sure I want people at all. Thanks Owen

Some designers are not reading the brief or previous messages. If you do more then once I will simply not comment and eliminate ask not to provide any more.

please stop using pictures and/or logos that imply - I manage their money - I protect their money - I grow their money - I offer homes loans - that I do house calls with individuals (i.e no couples shaking heads with a guy) - no house pictures or symbols i.e. it looks like a property website - I have a large organisation (i.e. team of people) If any design include the above I will eliminate it REMEMBER: I am providing innovative financial solutions - NOT asset/fund manager, bank manager or real estate manager thank you

All Please be creative and innovative with your pics. Also ensure you have the rights to use the pics. I have seen basic stock photos being used and again have not read by brief or previous comments. For instance, they use the words "sustainable growth" in google and click on images and you will see most of the images being used. these will be eliminated instantly and not asked to return.

Please, if you use the name of the Company as a Label or Statement can please ensure it remains in the same style as the Logo, i.e. all Caps Large with small.

All, I have decided that I don't want to have people in the main pic on the front page so please provide other inspirational pics. Thanks

guys I found a coffee advert whilst in Vietnam. I like the colour selection and thought it would be inspirational.i ahve added it yo my bried f

Real Estate

Coded - Design and coding required

```html
<!DOCTYPE html>
<html lang="en">
<head>
<meta charset="utf-8">
<title>Fernhold Capital</title>
<link rel="stylesheet" href="https://fonts.googleapis.com/css2?family=Cinzel:wght@400;700&family=Lora:ital,wght@0,400;0,700;1,400&family=Montserrat:wght@700&display=swap">
<style>
:root{
  --gold:#a8892a;
  --gold-dark:#8c7120;
  --ink:#222222;
  --text:#555555;
  --muted:#888888;
  --line:#e2e2e2;
  --band-blue:#d7ecfb;
  --concrete:#e6e6e6;
  --faq-bar:#d6d6d6;
  --testi-bg:#e9e9e9;
  --footer:#7f7f7f;
  --white:#ffffff;
}
*{margin:0;padding:0;box-sizing:border-box}
html,body{width:1200px;height:3064px;overflow:hidden}
body{font-family:"Lora",Georgia,serif;color:var(--text);background:var(--white);position:relative}
.wrap{width:1040px;margin:0 auto;position:relative}

/* top bar */
.topbar{height:36px;border-bottom:1px solid var(--line);font-size:13px;color:#444}
.topbar .wrap{height:36px;display:flex;align-items:center;gap:36px}
.topbar .hl{color:var(--gold)}
.topbar .search{position:absolute;right:0;top:9px}

/* header */
.header{height:122px}
.header .wrap{height:122px;display:flex;align-items:center;justify-content:space-between}
.brand{display:flex;align-items:center;gap:14px}
.brand-mark{width:42px;height:42px;background:var(--gold)}
.brand-name{font-family:"Cinzel",serif;font-weight:700;font-size:28px;color:var(--ink);letter-spacing:1px}
.nav{display:flex;gap:36px;font-family:"Lora",serif;font-size:17px;color:var(--ink);text-transform:uppercase}
.nav a{color:inherit;text-decoration:none;padding-bottom:8px}
.nav a.active{color:var(--gold);border-bottom:2px solid var(--gold)}

/* hero */
.hero{height:608px;position:relative;overflow:hidden}
.hero-photo{position:absolute;inset:0;background:radial-gradient(ellipse at 50% 30%,#8a8a8a 0%,#4a4540 45%,#1d1b1a 100%)}
.hero-content{position:relative;text-align:center;padding-top:250px;color:var(--white)}
.hero-title{font-family:"Montserrat",sans-serif;font-weight:700;font-size:50px;line-height:60px;letter-spacing:1px;text-transform:uppercase}
.hero-sub{font-family:"Lora",serif;font-style:italic;font-size:17px;line-height:26px;width:1040px;margin:22px auto 0}
.btn-more{display:inline-flex;align-items:center;gap:12px;margin-top:24px;background:var(--gold);color:var(--white);font-family:"Lora",serif;font-size:19px;padding:0 10px 0 26px;height:50px;border-radius:25px}
.btn-more .circ{width:34px;height:34px;border:2px solid var(--white);border-radius:50%;display:flex;align-items:center;justify-content:center}
.dots{position:absolute;left:0;right:0;bottom:14px;display:flex;justify-content:center;gap:6px}
.dots span{width:22px;height:22px;border-radius:50%;background:#666}
.dots span.on{background:#ddd;border:3px solid #888}

/* welcome */
.welcome{height:357px;text-align:center;padding-top:60px}
.sec-title{font-family:"Cinzel",serif;font-size:36px;color:var(--ink);font-weight:400}
.rule{width:36px;height:3px;background:var(--gold);margin:18px auto 0}
.welcome p{width:1000px;margin:30px auto 0;font-size:14px;line-height:23px;color:var(--text)}
.welcome p+p{margin-top:25px}

/* lending band */
.band{height:251px;background:var(--band-blue);position:relative;overflow:hidden}
.band .wrap{padding-top:30px}
.band h2{font-family:"Lora",serif;font-weight:700;font-size:31px;color:var(--ink)}
.band p{width:840px;font-size:14px;line-height:22px;margin-top:18px}
.band .more{color:#3d84c6;font-size:14px}
.band-deco{position:absolute;left:810px;top:0;width:230px;height:251px;border-radius:50%;background:radial-gradient(circle,rgba(150,190,225,.55),rgba(150,190,225,0) 70%)}

/* services */
.services{height:393px;background:var(--concrete)}
.services .wrap{display:flex;justify-content:space-between;padding-top:73px}
.card{width:325px;height:251px;background:var(--white);box-shadow:0 1px 4px rgba(0,0,0,.15);padding:22px 24px}
.card-icon{width:54px;height:54px;border:1px solid #ccc;border-radius:50%;display:flex;align-items:center;justify-content:center}
.card h3{font-family:"Lora",serif;font-weight:700;font-size:18px;color:var(--ink);margin-top:22px}
.card p{font-size:13px;line-height:20px;margin-top:10px;color:var(--text)}
.card .alert{color:var(--gold);font-weight:700;font-size:18px;margin-top:22px}
.card .big{font-size:21px;line-height:26px;color:var(--text);margin-top:8px}
.card .mail{font-size:15px;margin-top:8px;color:var(--text)}

/* faq */
.faq{height:569px;text-align:center;padding-top:50px}
.accordion{width:860px;margin:42px auto 0;text-align:left}
.acc-head{height:48px;display:flex;align-items:center;background:var(--faq-bar);font-family:"Lora",serif;font-size:22px;color:#777;text-transform:uppercase;margin-bottom:5px}
.acc-head .sign{width:48px;height:48px;background:var(--gold);color:var(--white);font-size:30px;display:flex;align-items:center;justify-content:center;margin-right:20px;font-family:"Montserrat",sans-serif}
.acc-head.open{background:var(--gold);color:var(--white)}
.acc-head.open .sign{background:var(--gold-dark)}
.acc-body{font-size:14px;line-height:23px;color:var(--text);padding:12px 10px 22px}

/* testimonials */
.testimonials{height:434px;background:var(--testi-bg);text-align:center;padding-top:62px;position:relative}
.testi-row{display:flex;justify-content:space-between;width:960px;margin:40px auto 0;text-align:left}
.testi{width:290px;display:flex;gap:12px}
.quote{font-family:"Lora",serif;font-size:70px;line-height:50px;color:#888;font-weight:700}
.testi p{font-size:12.5px;line-height:19px;color:#777}
.testi .name{font-size:13px;color:var(--ink);margin-top:12px}
.avatar{width:64px;height:64px;border-radius:50%;background:#bdbdbd;border:3px solid var(--white);margin-top:14px}
.arrow{position:absolute;top:200px}

/* footer */
.footer{height:294px;background:var(--footer);color:var(--white);position:relative}
.footer .cols{position:absolute;top:44px;left:0;width:1200px}
.fcol{position:absolute;top:0}
.fcol h4{font-family:"Lora",serif;font-size:17px;font-weight:400;margin-bottom:8px}
.fcol li{list-style:none;font-size:12.5px;line-height:17px}
.social{position:absolute;left:962px;top:50px;display:flex;gap:14px}
.social span{width:42px;height:42px;border:1px solid rgba(255,255,255,.9)}
.footline{position:absolute;left:84px;right:84px;top:238px;height:1px;background:rgba(255,255,255,.35)}
.copy{position:absolute;left:84px;right:84px;top:254px;font-size:11px;display:flex;justify-content:space-between;text-transform:uppercase}
.copy .links{display:flex;gap:18px}
</style>
</head>
<body>

<div class="topbar">
  <div class="wrap">
    <span>In case of any Questions, Please Call: <span class="hl">+11 555-0142</span></span>
    <span>Email: <span class="hl">info@fernholdcapital.com</span></span>
    <svg class="search" width="18" height="18" viewBox="0 0 18 18"><circle cx="7.5" cy="7.5" r="5.5" fill="none" stroke="#333" stroke-width="2"/><line x1="11.5" y1="11.5" x2="16.5" y2="16.5" stroke="#333" stroke-width="2"/></svg>
  </div>
</div>

<header class="header">
  <div class="wrap">
    <div class="brand"><span class="brand-mark"></span><span class="brand-name">Fernhold Capital</span></div>
    <nav class="nav">
      <a class="active">Home</a><a>About Us</a><a>Services</a><a>Funding Options</a><a>Contact Us</a>
    </nav>
  </div>
</header>

<section class="hero">
  <div class="hero-photo" role="img" aria-label="Close-up photo of hands fitting two white puzzle pieces together"></div>
  <div class="hero-content">
    <h1 class="hero-title">Lorem ipsum dolor sit amet<br>consectetur adipiscing elit</h1>
    <p class="hero-sub">Sed ut perspiciatis unde omnis iste natus error sit voluptatem accusantium doloremque laudantium, totam rem aperiam, eaque ipsa quae ab illo inventore veritatis et quasi architecto beatae vitae dicta sunt explicabo.</p>
    <span class="btn-more">Learn More <span class="circ"><svg width="12" height="14" viewBox="0 0 12 14"><path d="M3 2l6 5-6 5" fill="none" stroke="#fff" stroke-width="2.5"/></svg></span></span>
  </div>
  <div class="dots"><span class="on"></span><span></span><span></span><span></span><span></span></div>
</section>

<section class="welcome">
  <h2 class="sec-title">Welcome to Fernhold Capital</h2>
  <div class="rule"></div>
  <p>Lorem ipsum dolor sit amet, consectetur adipiscing elit, sed do eiusmod tempor incididunt ut labore et dolore magna aliqua. Ut enim ad minim veniam, quis nostrud exercitation ullamco laboris nisi ut aliquip ex ea commodo consequat. Duis aute irure dolor in reprehenderit in voluptate velit esse cillum dolore eu fugiat nulla pariatur. Excepteur sint occaecat cupidatat non proident, sunt in culpa qui officia deserunt mollit anim id est laborum.</p>
  <p>Lorem ipsum dolor sit amet, consectetur adipiscing elit, sed do eiusmod tempor incididunt ut labore et dolore magna aliqua. Ut enim ad minim veniam, quis nostrud exercitation ullamco laboris nisi ut aliquip ex ea commodo consequat. Duis aute irure dolor in reprehenderit in voluptate velit esse cillum dolore eu fugiat nulla pariatur. Excepteur sint occaecat cupidatat non proident, sunt in culpa qui officia deserunt mollit anim id est laborum.</p>
</section>

<section class="band">
  <div class="band-deco" role="img" aria-label="Faint globe decoration"></div>
  <div class="wrap">
    <h2>Over $700 million lent to small businesses globally</h2>
    <p>Lorem ipsum dolor sit amet, consectetur adipiscing elit, sed do eiusmod tempor incididunt ut labore et dolore magna aliqua. Ut enim ad minim veniam, quis nostrud exercitation ullamco laboris nisi ut aliquip ex ea commodo consequat.</p>
    <span class="more">Learn more</span>
  </div>
</section>

<section class="services">
  <div class="wrap">
    <div class="card">
      <div class="card-icon"><svg width="26" height="28" viewBox="0 0 26 28"><path d="M9 2h8l-3 5h-2z" fill="#333"/><path d="M10 8h6c5 4 8 9 8 13 0 4-3 6-11 6S2 25 2 21c0-4 3-9 8-13z" fill="#333"/><text x="13" y="23" font-size="10" fill="#fff" text-anchor="middle" font-family="Lora,serif">$</text></svg></div>
      <h3>Financing</h3>
      <p>Lorem ipsum dolor sit amet, consectetur adipiscing elit, sed do eiusmod tempor incididunt ut labore et dolore magna aliqua.</p>
    </div>
    <div class="card">
      <div class="card-icon"><svg width="26" height="26" viewBox="0 0 26 26"><rect x="4" y="3" width="18" height="21" fill="#333"/><g fill="#fff"><rect x="7" y="6" width="3" height="3"/><rect x="12" y="6" width="3" height="3"/><rect x="17" y="6" width="3" height="3" transform="translate(-1 0)"/><rect x="7" y="11" width="3" height="3"/><rect x="12" y="11" width="3" height="3"/><rect x="16" y="11" width="3" height="3"/><rect x="11" y="17" width="4" height="7"/></g></svg></div>
      <h3>Foreclosure Services</h3>
      <p>Lorem ipsum dolor sit amet, consectetur adipiscing elit, sed do eiusmod tempor incididunt ut labore et dolore magna aliqua.</p>
    </div>
    <div class="card">
      <div class="card-icon"><svg width="26" height="26" viewBox="0 0 26 26"><rect x="5" y="2" width="14" height="22" rx="2" fill="none" stroke="#333" stroke-width="2"/><line x1="9" y1="8" x2="16" y2="8" stroke="#333" stroke-width="2"/><line x1="9" y1="12" x2="16" y2="12" stroke="#333" stroke-width="2"/><circle cx="12" cy="20" r="1.5" fill="#333"/></svg></div>
      <p class="alert">Allow 24hrs. for response.</p>
      <p class="big">All Serious inquiries must be in writing.</p>
      <p class="mail">inquiry@fernholdcapital.com</p>
    </div>
  </div>
</section>

<section class="faq">
  <h2 class="sec-title">FAQs</h2>
  <div class="rule"></div>
  <div class="accordion">
    <div class="acc-head open"><span class="sign">−</span>Lorem ipsum dolor sit amet, consectetur adipiscing elit</div>
    <div class="acc-body">Lorem ipsum dolor sit amet, consectetur adipiscing elit, sed do eiusmod tempor incididunt ut labore et dolore magna aliqua. Ut enim ad minim veniam, quis nostrud exercitation ullamco laboris nisi ut aliquip ex ea commodo consequat. Duis aute irure dolor in reprehenderit in voluptate velit esse cillum dolore eu fugiat nulla pariatur. Excepteur sint occaecat cupidatat non proident, sunt in culpa qui officia deserunt mollit anim id est laborum. Lorem ipsum dolor sit amet, consectetur adipiscing elit, sed do eiusmod tempor incididunt ut labore et dolore magna aliqua.</div>
    <div class="acc-head"><span class="sign">+</span>Sed do eiusm labore et dolore magna aliqua.</div>
    <div class="acc-head"><span class="sign">+</span>Lorem ipsum dolor sit amet, consectetur adipiscing elit</div>
    <div class="acc-head"><span class="sign">+</span>Sed do eiusm labore et dolore magna aliqua.</div>
  </div>
</section>

<section class="testimonials">
  <h2 class="sec-title">Testimonials</h2>
  <div class="rule"></div>
  <svg class="arrow" style="left:86px" width="16" height="30" viewBox="0 0 16 30"><path d="M14 2L2 15l12 13" fill="none" stroke="#c8c8c8" stroke-width="2"/></svg>
  <svg class="arrow" style="right:86px" width="16" height="30" viewBox="0 0 16 30"><path d="M2 2l12 13L2 28" fill="none" stroke="#c8c8c8" stroke-width="2"/></svg>
  <div class="testi-row">
    <div class="testi"><span class="quote">“</span><div><p>Lorem ipsum dolor sit amet, consectetur adipiscing elit, sed do eiusmod tempor incididunt ut labore et dolore magna aliqua.</p><p class="name">Daniel Marlowe</p><div class="avatar" role="img" aria-label="Client portrait"></div></div></div>
    <div class="testi"><span class="quote">“</span><div><p>Lorem ipsum dolor sit amet, consectetur adipiscing elit, sed do eiusmod tempor incididunt ut labore et dolore magna aliqua.</p><p class="name">Tom Halvorsen</p><div class="avatar" role="img" aria-label="Client portrait"></div></div></div>
    <div class="testi"><span class="quote">“</span><div><p>Lorem ipsum dolor sit amet, consectetur adipiscing elit, sed do eiusmod tempor incididunt ut labore et dolore magna aliqua.</p><p class="name">Daniel Marlowe</p><div class="avatar" role="img" aria-label="Client portrait"></div></div></div>
  </div>
</section>

<footer class="footer">
  <div class="cols">
    <div class="fcol" style="left:84px"><h4>Capital Circle</h4><ul><li>Small business loans</li><li>Commercial loan comparison</li></ul></div>
    <div class="fcol" style="left:332px"><h4>How it works</h4><ul><li>Invest in small business</li><li>FAQ</li></ul></div>
    <div class="fcol" style="left:541px"><h4>About us</h4><ul><li>Our company</li><li>Team</li><li>Careers</li><li>Blog</li><li>Newsroom</li></ul></div>
    <div class="fcol" style="left:692px"><h4>Get in touch</h4><ul><li>support@fernholdcapital.com</li><li>+11 555-0142</li><li>Contact us</li></ul></div>
  </div>
  <div class="social" aria-label="Social media links"><span></span><span></span><span></span></div>
  <div class="footline"></div>
  <div class="copy"><span>Copyright ©2016 Fernhold Capital. All rights reserved.</span><span class="links"><span>Privacy Policy</span><span>Terms of Use</span></span></div>
</footer>

</body>
</html>
```